Defend science flier

Put my name and text below on one side of flier, and place other text on other side. Try to keep file about 4 by 6 or 6 by 8 inches.

Target Market(s)

Community and retailers.

Industry/Entity Type

Retail and concerned community.

Font styles to use
Serif

Requirements
Must have
• Good, eye-catching titles. Be smaller format. Not 8 by 11
Nice to have
• Black and white text. Maybe bullets etc for organizion but no decorations.
Should not have
• Any decoration

```html
<!DOCTYPE html>
<html lang="en">
<head>
<meta charset="utf-8">
<title>Martin R. Holloway, Ph.D — Flyer</title>
<link rel="stylesheet" href="https://fonts.googleapis.com/css2?family=Tinos:wght@400;700&family=PT+Sans:ital,wght@0,400;0,700;1,400&display=swap">
<style>
  :root {
    --gold: #b0924f;
    --gold-light: #d6c28e;
    --stone-light: #e4dccb;
    --stone-mid: #cbbd9c;
    --panel: #fdfdf8;
    --ink: #111111;
    --white: #ffffff;
  }
  * { box-sizing: border-box; margin: 0; padding: 0; }
  html, body {
    width: 1200px;
    height: 960px;
    overflow: hidden;
    background: var(--white);
  }
  .flyer {
    position: relative;
    width: 1200px;
    height: 960px;
  }
  .flyer-backdrop {
    position: absolute;
    inset: 0;
    background:
      linear-gradient(180deg, rgba(255,255,255,0) 55%, rgba(176,146,79,0.55) 100%),
      linear-gradient(90deg, var(--stone-mid) 0%, var(--stone-light) 4%, var(--stone-mid) 8%, var(--gold-light) 14%, var(--gold) 28%, var(--gold) 72%, var(--gold-light) 86%, var(--stone-mid) 92%, var(--stone-light) 96%, var(--stone-mid) 100%);
  }
  .content-panel {
    position: absolute;
    left: 58px;
    right: 58px;
    top: 54px;
    bottom: 58px;
    background: var(--panel);
    border-radius: 12px;
    color: var(--ink);
  }
  .flyer-header {
    text-align: center;
    padding-top: 70px;
  }
  .flyer-title {
    font-family: "Tinos", "Times New Roman", serif;
    font-weight: 400;
    font-size: 52px;
    line-height: 1.1;
  }
  .flyer-tagline {
    font-family: "Tinos", "Times New Roman", serif;
    font-size: 24px;
    margin-top: 26px;
  }
  .tagline-rule {
    display: block;
    margin: 22px auto 0;
    width: 440px;
    height: 6px;
  }
  .claims {
    list-style: none;
    margin: 56px 80px 0 52px;
    font-family: "PT Sans", "Segoe UI", sans-serif;
    font-size: 21px;
    line-height: 1.4;
  }
  .claim {
    position: relative;
    padding-left: 32px;
    margin-bottom: 26px;
  }
  .claim-icon {
    position: absolute;
    left: 0;
    top: 4px;
    width: 20px;
    height: 20px;
  }
  .endorsement-quote {
    margin: 10px 80px 0 84px;
    font-family: "PT Sans", "Segoe UI", sans-serif;
    font-style: italic;
    font-size: 21px;
    line-height: 1.55;
    text-align: justify;
  }
  .flyer-footer {
    position: absolute;
    left: 0;
    right: 0;
    top: 702px;
    text-align: center;
  }
  .homepage-label {
    font-family: "Tinos", "Times New Roman", serif;
    font-size: 25px;
    letter-spacing: 0.3px;
  }
  .homepage-link {
    display: block;
    width: 576px;
    height: 48px;
    margin: 14px auto 0;
    border-radius: 24px;
    background: var(--gold);
    color: var(--white);
    font-family: "PT Sans", "Segoe UI", sans-serif;
    font-size: 27px;
    line-height: 48px;
    text-decoration: none;
  }
</style>
</head>
<body>
<main class="flyer">
  <div class="flyer-backdrop" role="img" aria-label="Photograph of classical stone columns framing the flyer on a warm gold background"></div>

  <section class="content-panel">
    <header class="flyer-header">
      <h1 class="flyer-title">Martin R. Holloway, Ph.D</h1>
      <p class="flyer-tagline">“The Ashford and Kellerman of Psychology and History.”</p>
      <svg class="tagline-rule" viewBox="0 0 440 6" aria-hidden="true">
        <path d="M0 3 Q220 -1 440 3 Q220 7 0 3 Z" fill="var(--gold)"/>
      </svg>
    </header>

    <ul class="claims">
      <li class="claim">
        <svg class="claim-icon" viewBox="0 0 20 20" aria-hidden="true">
          <circle cx="10" cy="10" r="8.5" fill="none" stroke="var(--gold)" stroke-width="1.6"/>
          <path d="M8 6 L12 10 L8 14" fill="none" stroke="var(--gold)" stroke-width="1.8"/>
        </svg>
        Martin’s Bio-Psych has Restructured the Liberal Arts and Sciences—from Genetics to the Fine Arts and Hollywood.
      </li>
      <li class="claim">
        <svg class="claim-icon" viewBox="0 0 20 20" aria-hidden="true">
          <circle cx="10" cy="10" r="8.5" fill="none" stroke="var(--gold)" stroke-width="1.6"/>
          <path d="M8 6 L12 10 L8 14" fill="none" stroke="var(--gold)" stroke-width="1.8"/>
        </svg>
        Museum Catalogues, Better Nonfiction, and Hollywood Films Now Use Martin’s Methods.
      </li>
      <li class="claim">
        <svg class="claim-icon" viewBox="0 0 20 20" aria-hidden="true">
          <circle cx="10" cy="10" r="8.5" fill="none" stroke="var(--gold)" stroke-width="1.6"/>
          <path d="M8 6 L12 10 L8 14" fill="none" stroke="var(--gold)" stroke-width="1.8"/>
        </svg>
        Martin’s Biopsych is endorsed by Dr. R. Colin Marsh, professor of psychiatry at Eastbrook Medical School, who said:
      </li>
    </ul>

    <blockquote class="endorsement-quote">
      “Modern sleep and dream research teaches us-as does Martin Holloway’s book Human Mind or Social Mind-that all human activities, including art and politics, are products of the human brain, and that each of us has the privilege and responsibility of using it and communicating its creations.”
    </blockquote>

    <footer class="flyer-footer">
      <p class="homepage-label">SEE MARTIN’S HOMEPAGE FOR MORE DETAILS:</p>
      <a class="homepage-link" href="#">www.martin-holloway.org</a>
    </footer>
  </section>
</main>
</body>
</html>
```